Wordpress Lifestyle Blog

Just to be clear - I have the domain and the wordpress site (which is messy). I need someone to help me complete a simple blog design and then go into the existing wordpress site, and get rid of all the existing rubbish and set up the templates please. If we progress with design can we please be clear about additional costs upfront which, of course, I appreciate is the case.

Need a lifestyle blog. It is called brightyearsahead.com. Aimed at the older woman but needs to look fresh and young, not old fashioned. Navigation will be Home, Fashion, Feelings, Fitness, Contact. I have a logo but not sure it will work at the moment so happy with stylised words.Will have social media links.

Need homepage (not overly long) to have a main slider for pics/videos. Then the three category boxes underneath linking through to 2nd level pages containing blogs for that category and then the actual blog page. Happy to be led by expertise if this is not gonna work.

Am really looking for something clean and fresh like a Marwyn type approach to be honest.

If you need any further direction please just ask - once design chosen I am looking to move quickly.

Thank you so much for looking at this brief

Target Market(s)

Women, 40 - 60 age group but with a younger outlook

Number of Pages Required

3 page

Colors

Designer to choose colors to be used in the design.

Requirements
Must have
• Reflect youth, fun, bright
• Lift easily into a wordpress format
Should not have
• Old, staid, frumpy,dark

```html
<!DOCTYPE html>
<html lang="en">
<head>
<meta charset="utf-8">
<title>brightyearsahead.com — Home</title>
<link href="https://fonts.googleapis.com/css2?family=Montserrat:wght@400;500;600;700;800&family=Sacramento&display=swap" rel="stylesheet">
<style>
:root{
  --pink:#ec3f86;
  --pink-soft:#f7c6da;
  --ink:#222226;
  --muted:#8d8d93;
  --rule:#e6e6ea;
  --page:#ffffff;
  --white:#ffffff;
}
*{box-sizing:border-box;margin:0;padding:0}
html,body{width:1200px;height:2364px;overflow:hidden;background:var(--page)}
body{font-family:"Montserrat",Arial,sans-serif;color:var(--ink);position:relative}

/* header */
.site-header{position:absolute;left:88px;top:0;width:1024px;height:60px;display:flex;align-items:center;justify-content:space-between}
.main-nav{display:flex;gap:30px;width:340px;font-size:13px;font-weight:600;letter-spacing:.08em;text-transform:uppercase}
.main-nav.right{justify-content:flex-end}
.brand{font-size:26px;font-weight:800;letter-spacing:.02em;color:var(--pink)}

/* shared tile */
.photo{position:absolute;overflow:hidden}
.fill{position:absolute;inset:0}
.play{position:absolute;width:96px;height:96px;left:50%;top:50%;transform:translate(-50%,-50%)}
.caption-bar{position:absolute;left:18px;top:16px;display:flex;align-items:center;gap:10px;color:var(--white);font-size:12px;font-weight:700;letter-spacing:.06em;text-transform:uppercase}
.caption-bar .mark{width:14px;height:14px;background:var(--pink)}

/* hero */
.hero{left:88px;top:72px;width:680px;height:380px}
.profile{position:absolute;left:784px;top:72px;width:328px;height:380px;background:var(--pink);color:var(--white);text-align:center;padding:28px 30px}
.avatar{width:96px;height:96px;border-radius:50%;margin:0 auto 18px;border:4px solid var(--white);background:linear-gradient(135deg,#d9c2b2,#6b5a52)}
.profile-name{font-size:15px;font-weight:700;letter-spacing:.1em}
.profile-bio{font-size:12px;line-height:1.7;margin:12px 0 16px}
.profile-link{font-size:11px;font-weight:700;letter-spacing:.12em;border-bottom:1px solid var(--white);display:inline-block;padding-bottom:3px}
.social{display:flex;justify-content:center;gap:14px;margin-top:26px}
.social span{width:18px;height:18px;border-radius:50%;background:var(--white);opacity:.9}

/* grid rows */
.tile{position:absolute;width:328px;height:328px;overflow:hidden}
.col1{left:88px}.col2{left:436px}.col3{left:784px}
.tile .card-body{position:absolute;left:0;right:0;bottom:0;background:var(--white);padding:14px 18px 16px}
.kicker{font-size:11px;font-weight:700;letter-spacing:.1em;color:var(--pink);text-transform:uppercase}
.kicker span{color:var(--muted);font-weight:500;margin-left:6px}
.card-title{font-size:19px;font-weight:700;line-height:1.2;text-transform:uppercase;margin-top:6px;color:var(--ink)}
.btn-pair{position:absolute;left:18px;bottom:18px;display:flex;gap:10px}
.btn-pair span{background:var(--white);font-size:10px;font-weight:700;letter-spacing:.08em;padding:9px 12px;text-transform:uppercase}
.overlay-title{position:absolute;left:20px;top:54px;color:var(--white);font-size:26px;font-weight:600;letter-spacing:.1em}
.overlay-title em{display:block;font-family:"Sacramento",cursive;font-style:normal;font-size:64px;letter-spacing:0;line-height:.9;margin-top:6px}

/* feature banner */
.banner{left:88px;top:1172px;width:1024px;height:316px}
.banner-copy{position:absolute;left:40px;top:70px}
.banner-copy p{font-size:30px;line-height:1.25;letter-spacing:.06em;color:var(--ink);font-weight:500}
.banner-copy strong{font-weight:800}
.banner-btn{display:inline-block;margin-top:22px;background:var(--pink);color:var(--white);font-size:18px;font-weight:700;letter-spacing:.06em;padding:16px 26px}

/* footer */
.site-footer{position:absolute;left:88px;top:2272px;width:1024px;height:60px;border-top:1px solid var(--rule);display:flex;align-items:center;justify-content:space-between}
.footer-links{display:flex;gap:26px;width:340px;font-size:11px;font-weight:600;letter-spacing:.08em}
.footer-social{display:flex;gap:14px;width:340px;justify-content:flex-end}
.footer-social span{width:14px;height:14px;border-radius:50%;background:var(--ink)}
.site-footer .brand{font-size:22px}
</style>
</head>
<body>

<header class="site-header">
  <nav class="main-nav"><span>Home</span><span>Fashion</span><span>Feelings</span></nav>
  <div class="brand">BRIGHTYEARSAHEAD.COM</div>
  <nav class="main-nav right"><span>Videos</span><span>Fitness</span><span>Contact</span></nav>
</header>

<!-- hero video -->
<section class="photo hero">
  <div class="fill" role="img" aria-label="Video still of a woman with short blonde hair and red glasses working at a laptop in a bright living room" style="background:linear-gradient(120deg,#e8e6e3 0%,#b9b3ae 45%,#5d5754 75%,#cfcac6 100%)"></div>
  <div class="caption-bar"><span class="mark"></span>Summer Loomwell &amp; Hemline haul (with the dress I wore to my wedding!)</div>
  <svg class="play" viewBox="0 0 96 96"><circle cx="48" cy="48" r="45" fill="none" stroke="#fff" stroke-width="3"/><path d="M39 31 L66 48 L39 65 Z" fill="#fff"/></svg>
</section>

<aside class="profile">
  <div class="avatar" role="img" aria-label="Portrait of the blog author"></div>
  <div class="profile-name">LENA HARCOURT</div>
  <p class="profile-bio">A lifestyle blogger who writes on fashion, feelings and fitness for women who know their best years are still ahead.</p>
  <span class="profile-link">MORE ABOUT ME</span>
  <div class="social"><span></span><span></span><span></span><span></span><span></span></div>
</aside>

<!-- row 2 -->
<article class="tile col1" style="top:472px">
  <div class="fill" role="img" aria-label="Close-up of a tattooed arm with a striped top" style="background:linear-gradient(135deg,#3a2f2d,#c99a86 55%,#f0e4dc)"></div>
  <div class="card-body">
    <div class="kicker">Lifestyle <span>29th Apr 2018</span></div>
    <div class="card-title">Six tattoos later, my thoughts &amp; learnings</div>
  </div>
</article>
<article class="tile col2" style="top:472px">
  <div class="fill" role="img" aria-label="Woman lying on a teal sofa reading a magazine" style="background:linear-gradient(160deg,#f4f3ef,#5f8a86 55%,#2b4a4b)"></div>
  <div class="btn-pair"><span>Watch the video</span><span>Shop the look</span></div>
</article>
<article class="tile col3" style="top:472px">
  <div class="fill" role="img" aria-label="Woman in a red skirt walking past a green shopfront" style="background:linear-gradient(180deg,#3f6a4c,#8fa58f 50%,#b5423c 80%,#6e5d50)"></div>
</article>

<!-- row 3 -->
<article class="tile col1" style="top:820px">
  <div class="fill" role="img" aria-label="Woman in a blue top working on a laptop at home" style="background:linear-gradient(120deg,#bfbab4,#8d8680 50%,#4e5d7a)"></div>
  <div class="overlay-title">AT HOME<em>with</em></div>
</article>
<article class="tile col2" style="top:820px">
  <div class="fill" role="img" aria-label="Smiling woman in a slogan T-shirt sitting indoors" style="background:linear-gradient(135deg,#e9e4de,#cdbfae 60%,#9c8f84)"></div>
  <div class="card-body">
    <div class="kicker">Style <span>4th Apr 2018</span></div>
    <div class="card-title">Say it with a slogan</div>
  </div>
</article>
<article class="tile col3" style="top:820px">
  <div class="fill" role="img" aria-label="Woman in a white top and denim skirt on a town street" style="background:linear-gradient(180deg,#d8d6d2,#a9a7a4 50%,#6f7e96 80%,#3d3a38)"></div>
</article>

<!-- feature banner -->
<section class="photo banner">
  <div class="fill" role="img" aria-label="Woman holding a coffee cup outdoors against soft green foliage" style="background:linear-gradient(90deg,#f5f4f1 0%,#f1efea 42%,#e0b79c 62%,#b88770 72%,#9db77a 88%,#c7d9a6 100%)"></div>
  <div class="banner-copy">
    <p>IT'S NOT EVERY DAY A<br><strong>WOMAN IN HER LATE</strong></p>
    <span class="banner-btn">MY WEDDING</span>
  </div>
</section>

<!-- row 4 -->
<article class="tile col1" style="top:1512px">
  <div class="fill" role="img" aria-label="Woman in a blue top working on a laptop at home" style="background:linear-gradient(120deg,#bfbab4,#8d8680 50%,#4e5d7a)"></div>
  <div class="overlay-title">AT HOME<em>with</em></div>
</article>
<article class="tile col2" style="top:1512px">
  <div class="fill" role="img" aria-label="Smiling woman in a slogan T-shirt sitting indoors" style="background:linear-gradient(135deg,#e9e4de,#cdbfae 60%,#9c8f84)"></div>
  <div class="card-body">
    <div class="kicker">Style <span>4th Apr 2018</span></div>
    <div class="card-title">Say it with a slogan</div>
  </div>
</article>
<article class="tile col3" style="top:1512px">
  <div class="fill" role="img" aria-label="Woman with long silver hair in a floral top" style="background:linear-gradient(135deg,#8b8a88,#d9d6d2 45%,#4b4642 70%,#c28a3c)"></div>
</article>

<!-- row 5 -->
<article class="tile col1" style="top:1860px;height:368px">
  <div class="fill" role="img" aria-label="Video still of a smiling blonde woman in a light jacket" style="background:linear-gradient(135deg,#f2efe9,#d9c4ae 50%,#a7b07c)"></div>
  <svg class="play" viewBox="0 0 96 96"><circle cx="48" cy="48" r="45" fill="none" stroke="#fff" stroke-width="3"/><path d="M39 31 L66 48 L39 65 Z" fill="#fff"/></svg>
</article>
<article class="photo" style="left:436px;top:1860px;width:676px;height:368px">
  <div class="fill" role="img" aria-label="Video still of a blonde woman smiling in a garden" style="background:linear-gradient(120deg,#4f6b3a,#a3b27a 35%,#efe0cf 55%,#d5c0a6 70%,#5f7a44)"></div>
  <div class="caption-bar"><span class="mark"></span>Summer Loomwell &amp; Hemline haul (with the dress I wore to my wedding!)</div>
  <svg class="play" viewBox="0 0 96 96"><circle cx="48" cy="48" r="45" fill="none" stroke="#fff" stroke-width="3"/><path d="M39 31 L66 48 L39 65 Z" fill="#fff"/></svg>
</article>

<footer class="site-footer">
  <nav class="footer-links"><span>ABOUT ME</span><span>CONTACT</span><span>DISCLAIMER</span></nav>
  <div class="brand">BRIGHTYEARSAHEAD.COM</div>
  <div class="footer-social"><span></span><span></span><span></span><span></span><span></span></div>
</footer>

</body>
</html>
```